Professional PowerPoint Template for Data Reports, Presentations

We are a small leadership coaching/consulting firm and would like to update our PowerPoint template that we use with our clients, who are typically mid-senior level company professionals. I've attached a sample Powerpoint as well as our branding guide. The cover page is what needs the most work - just doesn't look current/professional enough. We do want to keep the pages after that clean, with come color but enough space for text and graphics.
Target Market(s)
Senior mgmt and HR executives in small-mid sized companies
Font styles to use
Sans Serif
Requirements
Must have
- Professional
- Clean
- Tied to company color scheme/logo
Nice to have
- Our title pages don't usually have many words on them; we'd like a design that has a lot of color - probably still using mainly our blue but accented with other colors.
- Need simple but smart looking pages after cover with lot of space; mostly we have text on the slides. Currently this is often in bullet point style, but we could probably upgrade the options there.
Should not have
- Anything that looks like a marketing style, as we typically use these with our current clients to share results of data collected, project plans, etc.

```html
<!DOCTYPE html>
<html lang="en">
<head>
<meta charset="utf-8">
<title>Corwell Presentation Template</title>
<link rel="stylesheet" href="https://fonts.googleapis.com/css2?family=Open+Sans:wght@400;600;700&family=PT+Sans:wght@400;700&display=swap">
<style>
:root{
  --navy:#1d4a7a;
  --blue:#1f5f9f;
  --blue-deep:#15406d;
  --blue-mid:#3c6e9f;
  --blue-soft:#4a7bab;
  --sky:#2a9fd8;
  --ink:#2f3033;
  --text:#555a60;
  --mark:#eceef1;
  --page:#ffffff;
  --chart-bg:#f2f3f5;
}
*{box-sizing:border-box;margin:0;padding:0}
html,body{width:1200px;height:2889px;overflow:hidden;background:var(--page)}
body{font-family:'Open Sans',Arial,sans-serif;color:var(--text)}
.board{position:relative;width:640px;height:1541px;transform:scale(1.875);transform-origin:0 0}

/* ---------- shared slide chrome ---------- */
.slide{position:absolute;width:270px;height:152px;background:#fff;overflow:hidden;box-shadow:0 1px 3px rgba(0,0,0,.2)}
.slide>*{position:absolute}
.slide-title{left:17px;top:11px;font:400 10px/1 'PT Sans',Arial,sans-serif;color:var(--navy);letter-spacing:.1px}
.brand{display:flex;align-items:center;gap:2px;font:700 4.6px/1 'Open Sans',Arial,sans-serif;letter-spacing:.9px;color:var(--navy)}
.brand-dot{width:4.6px;height:4.6px;border-radius:50%;background:currentColor}
.slide>.brand{right:10px;top:7px}
.footer{left:0;right:0;bottom:0;height:6px;background:var(--navy);color:#fff;font-size:2.3px;line-height:6px;text-align:center}
.footer .num{position:absolute;right:8px;top:0}
.mark{left:95px;top:30px;width:90px;height:90px;border-radius:50%;border:11px solid var(--mark)}
.copy{font-size:3.5px;line-height:4.6px;color:var(--text)}
.label{font:700 4.3px/1 'Open Sans',Arial,sans-serif;color:var(--ink);letter-spacing:.2px}
.overlay{left:0;top:0;width:270px;height:152px}

/* ---------- cover ---------- */
.cover{position:absolute;left:42px;top:8px;width:552px;height:310px;background:#fff;overflow:hidden;box-shadow:0 1px 3px rgba(0,0,0,.2)}
.cover>*{position:absolute}
.cover-band{left:0;top:0;width:552px;height:250px;background:linear-gradient(120deg,#2167a8 0%,var(--blue) 45%,var(--blue-deep) 100%)}
.cover-mark{left:18px;top:50px;width:150px;height:150px;border-radius:50%;border:22px solid rgba(255,255,255,.08)}
.cover-art{left:330px;top:0;width:222px;height:240px;background:radial-gradient(circle at 55% 45%,rgba(120,175,230,.35),rgba(120,175,230,.05) 70%)}
.cover-title{left:135px;top:80px;font:700 31px/35px 'Open Sans',Arial,sans-serif;color:#fff;letter-spacing:-.3px}
.cover-rule{left:137px;top:154px;width:90px;height:1.6px;background:#fff}
.cover-sub{left:142px;top:164px;font:400 10px/1 'Open Sans',Arial,sans-serif;color:#fff}
.cover .brand{left:40px;top:271px;font-size:19px;letter-spacing:2.6px;gap:8px;font-weight:600}
.cover .brand-dot{width:18px;height:18px}
.cover-date{right:30px;top:275px;font:700 10px/1 'Open Sans',Arial,sans-serif;color:var(--navy)}

/* ---------- three columns ---------- */
.icon-dot{width:13px;height:13px;border-radius:50%;background:var(--navy);display:flex;align-items:center;justify-content:center}
.col{width:72px;top:62px}
.col .label{margin-bottom:3px}

/* ---------- intro ---------- */
.sub-head{font:400 6px/1 'Open Sans',Arial,sans-serif;color:var(--ink)}
.art-round{border-radius:50%;background:radial-gradient(circle at 50% 50%,#27a9c4 0%,#1b8fb0 60%,#d9eef4 61%,#fff 72%)}

/* ---------- process bars ---------- */
.bar-item{left:118px;width:145px;background:var(--navy);color:#fff;font-size:3.5px;line-height:4.6px;padding:2px 4px 2px 16px}
.ring-mark{left:28px;top:50px;width:56px;height:56px;border-radius:50%;border:9px solid var(--navy)}
.bubble{width:22px;height:22px;border-radius:50%;background:var(--navy);border:1.6px solid #fff;box-shadow:0 0 0 .6px var(--navy);display:flex;align-items:center;justify-content:center}

/* ---------- photo with panel ---------- */
.photo{background:linear-gradient(135deg,#b8a894 0%,#7d6a58 45%,#d8d2c8 100%)}
.panel{left:100px;top:22px;width:148px;height:107px;background:rgba(29,67,110,.94);padding:16px 10px 0 12px;color:#fff}
.panel .panel-title{font:400 9px/1 'PT Sans',Arial,sans-serif;margin-bottom:5px}
.panel .copy{color:#e7eef6}

/* ---------- timeline ---------- */
.step{width:44px;text-align:center;top:110px}
.step .tri{width:0;height:0;margin:0 auto 2px;border-left:2px solid transparent;border-right:2px solid transparent;border-bottom:3px solid var(--ink)}
.step .label{font-size:3px;margin-bottom:1.5px}
.step .copy{font-size:3px;line-height:3.8px}

/* ---------- break ---------- */
.coffee{left:0;top:0;width:122px;height:146px;background:linear-gradient(160deg,#e6dccf 0%,#a77a52 45%,#3b2516 100%)}
.break-text{left:155px;top:84px;font:400 10px/1 'Open Sans',Arial,sans-serif;color:var(--ink)}
.break-rule{left:160px;top:100px;width:72px;height:.6px;background:#d7d9dc}

/* ---------- pie ---------- */
.side-block{width:102px}
.side-block .label{font-size:5px;margin-bottom:3px}

/* ---------- dashboard ---------- */
.monitor{left:28px;top:34px;width:94px;height:98px;background:linear-gradient(180deg,#dfe5ec 0%,#9aa6b3 55%,#f1f3f5 100%);border-radius:2px}

/* ---------- cards ---------- */
.card{width:65px;top:41px}
.card-head{height:20px;background:var(--navy);color:#fff;font:700 4.4px/1 'Open Sans',Arial,sans-serif;text-align:center;padding-top:10px}
.card-icon{position:absolute;left:26px;top:-7px;width:13px;height:13px;border-radius:50%;background:#1c1c1e;border:1.2px solid #fff;display:flex;align-items:center;justify-content:center}
.card .copy{color:var(--navy);text-align:center;padding-top:2px}
.card .copy.more{color:var(--text)}
.card u{color:var(--ink)}

/* ---------- swot ---------- */
.swot{width:87px;height:53px;background:linear-gradient(180deg,#31aee6 0%,#1280c6 100%);color:#fff;font-size:3.5px;line-height:4.6px;display:flex;align-items:center;justify-content:center;text-align:center;padding:0 12px}
.corner{width:12px;height:12px;border-radius:50%;background:#fff;border:1.2px solid var(--ink);font:700 5px/9.6px 'Open Sans',Arial,sans-serif;text-align:center;color:var(--ink)}

/* ---------- closing ---------- */
.closing{background:var(--navy)}
.closing .close-mark{left:18px;top:22px;width:92px;height:92px;border-radius:50%;border:14px solid rgba(255,255,255,.07)}
.closing .brand{left:112px;top:47px;color:#fff;font-size:5.5px}
.closing .brand-dot{width:5.5px;height:5.5px}
.thanks{left:110px;top:58px;font:400 23px/1 'Open Sans',Arial,sans-serif;color:#fff}
.closing .copy{left:112px;top:96px;color:#fff;font-size:3.3px;line-height:4.6px}
.closing .footer{background:#163a62}
</style>
</head>
<body>
<div class="board">

  <!-- Cover -->
  <section class="cover">
    <div class="cover-band"></div>
    <div class="cover-mark"></div>
    <div class="cover-art" role="img" aria-label="Line-art illustration of business icons and hands holding documents, phone and tools"></div>
    <h1 class="cover-title">PRESENTATION<br>TITLE HERE</h1>
    <div class="cover-rule"></div>
    <p class="cover-sub">Subtitle Here</p>
    <div class="brand"><span class="brand-dot"></span>CORWELL</div>
    <p class="cover-date">Aug 2018</p>
  </section>

  <!-- 1 Three columns -->
  <section class="slide" style="left:42px;top:330px">
    <div class="mark"></div>
    <h2 class="slide-title">SLIDE TITLE</h2>
    <div class="brand"><span class="brand-dot"></span>CORWELL</div>
    <div class="icon-dot" style="left:31px;top:43px"><svg width="7" height="7" viewBox="0 0 10 10"><circle cx="5" cy="3.3" r="2" fill="none" stroke="#fff" stroke-width="1"/><path d="M1.5 9.5c.5-2.6 2-3.6 3.5-3.6s3 1 3.5 3.6" fill="none" stroke="#fff" stroke-width="1"/></svg></div>
    <div class="icon-dot" style="left:111px;top:43px"><svg width="7" height="7" viewBox="0 0 10 10"><path d="M5 1l3.5 1.5v3c0 2-1.6 3.2-3.5 3.8C3.1 8.7 1.5 7.5 1.5 5.5v-3z" fill="none" stroke="#fff" stroke-width="1"/><path d="M3.4 5.2l1.2 1.2 2.2-2.4" fill="none" stroke="#fff" stroke-width="1"/></svg></div>
    <div class="icon-dot" style="left:192px;top:43px"><svg width="7" height="7" viewBox="0 0 10 10"><circle cx="5" cy="5" r="3.8" fill="none" stroke="#fff" stroke-width="1"/><path d="M5 2.6v4.8M6.4 3.6H4.4a1 1 0 000 2h1.2a1 1 0 010 2H3.6" fill="none" stroke="#fff" stroke-width=".8"/></svg></div>
    <div class="col" style="left:11px"><p class="label">SUBTITLE</p><p class="copy">Summarise the key finding for this area in a few short lines. Keep the language plain so senior readers can scan it quickly and move on to the next point with confidence.</p></div>
    <div class="col" style="left:108px"><p class="label">SUBTITLE</p><p class="copy">Summarise the key finding for this area in a few short lines. Keep the language plain so senior readers can scan it quickly and move on to the next point with confidence.</p></div>
    <div class="col" style="left:187px"><p class="label">SUBTITLE</p><p class="copy">Summarise the key finding for this area in a few short lines. Keep the language plain so senior readers can scan it quickly and move on to the next point with confidence.</p></div>
    <div class="footer">www.corwellcoaching.com | info@corwellcoaching.com<span class="num">1</span></div>
  </section>

  <!-- 2 Intro -->
  <section class="slide" style="left:325px;top:330px">
    <div class="mark"></div>
    <h2 class="slide-title">SLIDE TITLE</h2>
    <div class="brand"><span class="brand-dot"></span>CORWELL</div>
    <p class="sub-head" style="left:17px;top:46px">Subtitle</p>
    <p class="copy" style="left:17px;top:55px;width:108px">Use this space to introduce the topic of the slide. State what was measured, who took part and why it matters to the team. Close with one line that leads into the next section of the report.</p>
    <div class="art-round" style="left:138px;top:18px;width:118px;height:118px" role="img" aria-label="Illustration of two business people shaking hands in front of a blue circle with icons"></div>
    <div class="footer">www.corwellcoaching.com | info@corwellcoaching.com<span class="num">2</span></div>
  </section>

  <!-- 3 Process bars -->
  <section class="slide" style="left:42px;top:496px">
    <div class="mark"></div>
    <h2 class="slide-title">SLIDE TITLE</h2>
    <div class="brand"><span class="brand-dot"></span>CORWELL</div>
    <div class="ring-mark"></div>
    <svg class="overlay" viewBox="0 0 270 152"><path d="M96 20Q130 78 96 136" fill="none" stroke="var(--navy)" stroke-width=".6"/></svg>
    <p class="bar-item" style="top:39px;height:20px">Add a short statement here that explains the first result and what the team should take from it.</p>
    <p class="bar-item" style="top:69px;height:25px">Add a short statement here that explains the second result and what the team should take from it.</p>
    <p class="bar-item" style="top:103px;height:21px">Add a short statement here that explains the third result and what the team should take from it.</p>
    <div class="bubble" style="left:105px;top:38px"><svg width="10" height="10" viewBox="0 0 10 10"><circle cx="5" cy="3.3" r="2" fill="none" stroke="#fff" stroke-width=".9"/><path d="M1.5 9.5c.5-2.6 2-3.6 3.5-3.6s3 1 3.5 3.6" fill="none" stroke="#fff" stroke-width=".9"/></svg></div>
    <div class="bubble" style="left:110px;top:70px"><svg width="10" height="10" viewBox="0 0 10 10"><path d="M1 9h8M2.5 8V5M4.5 8V3M6.5 8V4.5M8.5 8V2" stroke="#fff" stroke-width=".9" fill="none"/></svg></div>
    <div class="bubble" style="left:105px;top:102px"><svg width="10" height="10" viewBox="0 0 10 10"><rect x="1.2" y="2" width="7.6" height="7" fill="none" stroke="#fff" stroke-width=".9"/><path d="M1.2 4h7.6M3.2 1v2M6.8 1v2M3 6h1M5 6h1M3 7.5h1M5 7.5h1" stroke="#fff" stroke-width=".8"/></svg></div>
    <div class="footer">www.corwellcoaching.com | info@corwellcoaching.com<span class="num">4</span></div>
  </section>

  <!-- 4 Photo with panel -->
  <section class="slide" style="left:325px;top:496px">
    <div class="photo" style="left:0;top:0;width:160px;height:146px" role="img" aria-label="Photo of colleagues in a meeting room"></div>
    <div class="brand"><span class="brand-dot"></span>CORWELL</div>
    <div class="panel">
      <h2 class="panel-title">SLIDE TITLE</h2>
      <p class="copy">Describe the setting of this session in a few lines. Explain who was in the room, what the group worked on and which questions came up most often. Note any agreements made and the actions that follow, with owners and dates where they are known. End with a short line about the next meeting.</p>
    </div>
    <div class="footer">www.corwellcoaching.com | info@corwellcoaching.com<span class="num">5</span></div>
  </section>

  <!-- 5 Timeline -->
  <section class="slide" style="left:42px;top:662px">
    <div class="mark"></div>
    <h2 class="slide-title">SLIDE TITLE</h2>
    <div class="brand"><span class="brand-dot"></span>CORWELL</div>
    <svg class="overlay" viewBox="0 0 270 152" font-family="Open Sans, Arial, sans-serif">
      <circle cx="198" cy="74" r="35" fill="var(--blue-soft)"/>
      <circle cx="142" cy="80" r="25" fill="var(--ink)"/>
      <circle cx="98" cy="84" r="19" fill="var(--blue-mid)"/>
      <circle cx="62" cy="88" r="14" fill="#3a3a3c"/>
      <text x="58" y="89.5" fill="#fff" font-size="3.6" text-anchor="middle">YEAR 1</text>
      <text x="98" y="86" fill="#fff" font-size="3.8" text-anchor="middle">YEAR 2</text>
      <text x="142" y="81.5" fill="#fff" font-size="4.2" text-anchor="middle">YEAR 3</text>
      <text x="201" y="75" fill="#fff" font-size="5" text-anchor="middle">YEAR 4</text>
    </svg>
    <div class="step" style="left:40px"><div class="tri"></div><p class="label">SUBTITLE</p><p class="copy">Short note on this stage of the plan.</p></div>
    <div class="step" style="left:78px"><div class="tri"></div><p class="label">SUBTITLE</p><p class="copy">Short note on this stage of the plan.</p></div>
    <div class="step" style="left:120px"><div class="tri"></div><p class="label">SUBTITLE</p><p class="copy">Short note on this stage of the plan.</p></div>
    <div class="step" style="left:174px"><div class="tri"></div><p class="label">SUBTITLE</p><p class="copy">Short note on this stage of the plan.</p></div>
    <div class="footer">www.corwellcoaching.com | info@corwellcoaching.com<span class="num">6</span></div>
  </section>

  <!-- 6 Charts -->
  <section class="slide" style="left:325px;top:662px">
    <div class="mark"></div>
    <h2 class="slide-title">SLIDE TITLE</h2>
    <div class="brand"><span class="brand-dot"></span>CORWELL</div>
    <svg class="overlay" viewBox="0 0 270 152" font-family="Open Sans, Arial, sans-serif">
      <text x="74" y="32" font-size="4" font-weight="700" fill="#333" text-anchor="middle">CHART TITLE</text>
      <g stroke="#e2e4e7" stroke-width=".3">
        <path d="M18 40H132M18 54H132M18 68H132M18 82H132M18 96H132M18 110H132"/>
      </g>
      <g font-size="2.6" fill="#888" text-anchor="end">
        <text x="15" y="41">6</text><text x="15" y="55">5</text><text x="15" y="69">4</text><text x="15" y="83">3</text><text x="15" y="97">2</text><text x="15" y="111">1</text>
      </g>
      <polyline points="28,92 63,70 98,82 128,60" fill="none" stroke="var(--navy)" stroke-width=".8"/>
      <polyline points="28,80 63,96 98,66 128,56" fill="none" stroke="#7fb0dc" stroke-width=".8"/>
      <polyline points="28,100 63,86 98,96 128,76" fill="none" stroke="#111" stroke-width=".8"/>
      <g font-size="2.6" fill="#888" text-anchor="middle">
        <text x="28" y="117">Year 1</text><text x="63" y="117">Year 2</text><text x="98" y="117">Year 3</text><text x="128" y="117">Year 4</text>
      </g>
      <g font-size="2.4" fill="#777">
        <rect x="40" y="121" width="5" height=".8" fill="var(--navy)"/><text x="46" y="122">Series 1</text>
        <rect x="62" y="121" width="5" height=".8" fill="#7fb0dc"/><text x="68" y="122">Series 2</text>
        <rect x="84" y="121" width="5" height=".8" fill="#111"/><text x="90" y="122">Series 3</text>
      </g>
      <rect x="148" y="23" width="114" height="107" fill="var(--chart-bg)"/>
      <text x="205" y="31" font-size="4" font-weight="700" fill="#333" text-anchor="middle">CHART TITLE</text>
      <g font-size="2.4" fill="#777">
        <rect x="172" y="35" width="4" height="2" fill="var(--navy)"/><text x="177" y="37">Series 1</text>
        <rect x="192" y="35" width="4" height="2" fill="#111"/><text x="197" y="37">Series 2</text>
        <rect x="212" y="35" width="4" height="2" fill="#c9ccd1"/><text x="217" y="37">Series 3</text>
      </g>
      <path d="M155 112H258" stroke="#bbb" stroke-width=".3"/>
      <g>
        <rect x="158" y="76" width="5" height="36" fill="var(--navy)"/><rect x="163" y="92" width="5" height="20" fill="#111"/><rect x="168" y="100" width="5" height="12" fill="#c9ccd1"/>
        <rect x="183" y="88" width="5" height="24" fill="var(--navy)"/><rect x="188" y="64" width="5" height="48" fill="#111"/><rect x="193" y="100" width="5" height="12" fill="#c9ccd1"/>
        <rect x="208" y="82" width="5" height="30" fill="var(--navy)"/><rect x="213" y="96" width="5" height="16" fill="#111"/><rect x="218" y="94" width="5" height="18" fill="#c9ccd1"/>
        <rect x="233" y="62" width="5" height="50" fill="var(--navy)"/><rect x="238" y="84" width="5" height="28" fill="#111"/><rect x="243" y="88" width="5" height="24" fill="#c9ccd1"/>
      </g>
      <g font-size="2.6" fill="#777" text-anchor="middle">
        <text x="165" y="117">YEAR 1</text><text x="190" y="117">YEAR 2</text><text x="215" y="117">YEAR 3</text><text x="240" y="117">YEAR 4</text>
      </g>
    </svg>
    <div class="footer">www.corwellcoaching.com | info@corwellcoaching.com<span class="num">7</span></div>
  </section>

  <!-- 7 Break -->
  <section class="slide" style="left:42px;top:828px">
    <div class="mark" style="left:150px"></div>
    <div class="coffee" role="img" aria-label="Photo of coffee cups on coffee beans"></div>
    <div class="brand"><span class="brand-dot"></span>CORWELL</div>
    <svg class="overlay" viewBox="0 0 270 152">
      <circle cx="197" cy="58" r="18" fill="#fff" stroke="#9aa3ad" stroke-width="1.4"/>
      <path d="M197 46V59H207" fill="none" stroke="#9aa3ad" stroke-width="1.4" stroke-linecap="round"/>
    </svg>
    <p class="break-text">Coffee Break!</p>
    <div class="break-rule"></div>
    <div class="footer">www.corwellcoaching.com | info@corwellcoaching.com<span class="num">8</span></div>
  </section>

  <!-- 8 Pie -->
  <section class="slide" style="left:325px;top:828px">
    <div class="mark"></div>
    <h2 class="slide-title">SLIDE TITLE</h2>
    <div class="brand"><span class="brand-dot"></span>CORWELL</div>
    <svg class="overlay" viewBox="0 0 270 152" font-family="Open Sans, Arial, sans-serif">
      <path d="M75 77L75 37A40 40 0 1 1 51.5 109.4Z" fill="var(--navy)" stroke="#fff" stroke-width=".8"/>
      <path d="M75 77L51.5 109.4A40 40 0 0 1 75 37Z" fill="#111" stroke="#fff" stroke-width=".8"/>
      <text x="98" y="76" font-size="7" font-weight="700" fill="#fff" text-anchor="middle">60%</text>
      <text x="98" y="81" font-size="2.8" fill="#fff" text-anchor="middle">Label text</text>
      <text x="55" y="64" font-size="6" font-weight="700" fill="#fff" text-anchor="middle">40%</text>
      <text x="55" y="68.5" font-size="2.8" fill="#fff" text-anchor="middle">Label text</text>
      <path d="M102 106L114 114" stroke="#999" stroke-width=".4"/>
      <rect x="112" y="113" width="40" height="20" rx="2" fill="#fff" stroke="#bbb" stroke-width=".4"/>
      <text x="132" y="120" font-size="2.6" fill="#555" text-anchor="middle">Short note on the</text>
      <text x="132" y="124" font-size="2.6" fill="#555" text-anchor="middle">total sample</text>
      <text x="132" y="130" font-size="3.6" font-weight="700" fill="#222" text-anchor="middle">100%</text>
      <rect x="42" y="125" width="3" height="1.6" fill="var(--navy)"/><text x="46" y="126.5" font-size="2.4" fill="#777">Category A</text>
      <rect x="64" y="125" width="3" height="1.6" fill="#111"/><text x="68" y="126.5" font-size="2.4" fill="#777">Category B</text>
      <text x="72" y="140" font-size="2.4" fill="#777" text-anchor="middle">*Source: your reference 2024</text>
    </svg>
    <div class="side-block" style="left:158px;top:51px">
      <p class="label">SUBTITLE</p>
      <p class="copy">Explain what the chart shows in a few lines. Point out the larger share first, then say what the smaller share means for the group and what should happen next.</p>
    </div>
    <div class="footer">www.corwellcoaching.com | info@corwellcoaching.com<span class="num">9</span></div>
  </section>

  <!-- 9 Dashboard -->
  <section class="slide" style="left:42px;top:994px">
    <div class="mark"></div>
    <h2 class="slide-title">SLIDE TITLE</h2>
    <div class="brand"><span class="brand-dot"></span>CORWELL</div>
    <div class="monitor" role="img" aria-label="Photo of a desktop computer showing a data dashboard"></div>
    <div class="side-block" style="left:155px;top:54px">
      <p class="label">SUBTITLE</p>
      <p class="copy">Describe the dashboard in a few lines. Point out the measures that moved most this quarter and explain what the team should watch in the weeks ahead.</p>
    </div>
    <div class="footer">www.corwellcoaching.com | info@corwellcoaching.com<span class="num">10</span></div>
  </section>

  <!-- 10 Cards -->
  <section class="slide" style="left:325px;top:994px">
    <div class="mark"></div>
    <h2 class="slide-title">SLIDE TITLE</h2>
    <div class="brand"><span class="brand-dot"></span>CORWELL</div>
    <div class="card" style="left:40px">
      <div class="card-head"><span class="card-icon"><svg width="7" height="7" viewBox="0 0 10 10"><path d="M2 8L8 2M5 2h3v3" fill="none" stroke="#fff" stroke-width="1"/></svg></span>Subtitle</div>
      <p class="copy">Add a brief point here about this topic and why it matters.</p>
      <p class="copy more">Support it with a second short line of detail for the reader to follow. <u>Read more</u></p>
    </div>
    <div class="card" style="left:115px">
      <div class="card-head"><span class="card-icon"><svg width="7" height="7" viewBox="0 0 10 10"><circle cx="5" cy="5" r="3.6" fill="none" stroke="#fff" stroke-width="1"/><path d="M4 3.4L6 5 4 6.6" fill="none" stroke="#fff" stroke-width="1"/></svg></span>Subtitle</div>
      <p class="copy">Add a brief point here about this topic and why it matters.</p>
      <p class="copy more">Support it with a second short line of detail for the reader to follow. <u>Read more</u></p>
    </div>
    <div class="card" style="left:190px">
      <div class="card-head"><span class="card-icon"><svg width="7" height="7" viewBox="0 0 10 10"><circle cx="5" cy="3.3" r="2" fill="none" stroke="#fff" stroke-width="1"/><path d="M1.5 9.5c.5-2.6 2-3.6 3.5-3.6s3 1 3.5 3.6" fill="none" stroke="#fff" stroke-width="1"/></svg></span>Subtitle</div>
      <p class="copy">Add a brief point here about this topic and why it matters.</p>
      <p class="copy more">Support it with a second short line of detail for the reader to follow. <u>Read more</u></p>
    </div>
    <div class="footer">www.corwellcoaching.com | info@corwellcoaching.com<span class="num">11</span></div>
  </section>

  <!-- 11 Empty -->
  <section class="slide" style="left:42px;top:1160px">
    <div class="mark"></div>
    <h2 class="slide-title">EMPTY SLIDE</h2>
    <div class="brand"><span class="brand-dot"></span>CORWELL</div>
    <div class="footer">www.corwellcoaching.com | info@corwellcoaching.com<span class="num">12</span></div>
  </section>

  <!-- 12 SWOT -->
  <section class="slide" style="left:325px;top:1160px">
    <div class="mark"></div>
    <h2 class="slide-title">SLIDE TITLE</h2>
    <div class="brand"><span class="brand-dot"></span>CORWELL</div>
    <p class="swot" style="left:44px;top:26px;border-radius:3px 3px 14px 3px">Key point for this quarter goes here in brief.</p>
    <p class="swot" style="left:134px;top:26px;border-radius:3px 3px 3px 14px">Key point for this quarter goes here in brief.</p>
    <p class="swot" style="left:44px;top:82px;border-radius:3px 14px 3px 3px">Key point for this quarter goes here in brief.</p>
    <p class="swot" style="left:134px;top:82px;border-radius:14px 3px 3px 3px">Key point for this quarter goes here in brief.</p>
    <span class="corner" style="left:38px;top:20px">S</span>
    <span class="corner" style="left:215px;top:20px">W</span>
    <span class="corner" style="left:38px;top:129px">T</span>
    <span class="corner" style="left:215px;top:129px">O</span>
    <div class="footer">www.corwellcoaching.com | info@corwellcoaching.com<span class="num">13</span></div>
  </section>

  <!-- Closing -->
  <section class="slide closing" style="left:205px;top:1338px">
    <div class="close-mark"></div>
    <div class="brand"><span class="brand-dot"></span>CORWELL</div>
    <p class="thanks">Thank you</p>
    <p class="copy"><b>Address goes here:</b> 100 Harbour Lane, Suite 4<br><b>www.corwellcoaching.com</b> | <b>hello@corwellcoaching.com</b></p>
    <div class="footer"></div>
  </section>

</div>
</body>
</html>
```